VidTrellis banner - Girl illustration, technology, green, blue, spring-like

I need help for vidtrellis art for my banner. There are strict channel art templates. I have no ideas at all but hope if you look at some of my videos you will learn a bit about me.

My channel:
https://www.vidtrellis.example/channel/QTZPfM2w8Lk3N7Hcdra5Ypx

My channel is on Unix, technology, information security, and some technical demonstration videos.

Channel templates can be found here
https://help.corvanthe.example/vidtrellis/answer/5816407?hl=en

Here is what I don't like:
- pictures of "hackers" - boys with hoodies on
- pictures of circuit boards

Can show my name "LP Thornbury" preferred, cursive is good, or blackboard type fun font

or "Lise-Paule Thornbury" is an option

vQuarn.ca is my company webpage, but we are not really using the logo or company name much so it does not need to feature
Updates

Oh, and I am Canadian and an outdoor lover :-) that means that silhouettes of maple leaves, and moose and other Canadian symbols would be something I like also...*AND* I recently caught my hair and now have bangs (fringe) so if you are making an image of me that is important. Also I have green eyes. - I will upload a photo. Added Thursday, November 24, 2016

Target Market(s)

My viewers are currently majority 25-35 year old males, but am trying to appeal to girls too.

Industry/Entity Type

Computer Security

Logo Text

LP Thornbury

Logo styles of interest
Pictorial/Combination Logo
Font styles to use
Sans Serif
Decorative
Script
Other font styles liked:
• Blackboard

Colors
33a6d7
33b8a4
00a990
3276b5
0255a3
6b449b
b7a5cd
fbee3e
faa54b

Requirements
Must have
• Must conform to the vidtrellis channel art template and look great on all devices: TV, computer, tablet and phone. 2560 x 1440 px and 4MB or smaller in JPEG or PNG format
• Channel templates can be found here
• https://help.corvanthe.example/vidtrellis/answer/5816407?hl=en
• On a TV display, the whole image is displayed as channel art. The aspect ratio is 16:9 (i.e. 2560 x 1440 px).
• Minimum width: 2048 X 1152 px. This is the "safe area," where text and logos are guaranteed not to be cut off when displayed on different devices.
• Maximum width: 2560 X 423 px. This means that the "safe area" is always visible; the areas to each side of the channel art are visible depending on the viewer’s browser size.
• File size: 4MB or smaller recommended.
• If you're not sure about the width and height of an image, download our Channel Art Templates to see how images show on different devices. You can use your computer's image editor or find one online to resize the images.
Nice to have
• I'm pretty open, but here is what I like:
• - colours blue, green, bright and spring like
• - unisex appeal
• - cool girl hackers are okay
• - I like birds, stylized doves are good, hummingbirds are a favorite
• - cartoon or anime girls may appeal to me. with dreadlocks or yarn-like hair are a bonus - if you do an illustration of me, I have green eyes and bangs (fringe)
• - design should be fun but elegant
Should not have
• Here is what I don't like:
• - pictures of "hackers" - boys with hoodies on
• - pictures of circuit boards

```html
<!DOCTYPE html>
<html lang="en">
<head>
<meta charset="utf-8">
<title>LP Thornbury — Channel Banner</title>
<link rel="stylesheet" href="https://fonts.googleapis.com/css2?family=Montserrat:wght@600&display=swap">
<style>
  :root {
    --bg: #62479a;
    --line: rgba(255, 255, 255, 0.22);
    --line-soft: rgba(255, 255, 255, 0.12);
    --accent-pink: rgba(214, 120, 200, 0.35);
    --glyph: #ffffff;
    --glyph-soft: rgba(255, 255, 255, 0.75);
  }
  html, body {
    margin: 0;
    padding: 0;
    overflow: hidden;
    background: var(--bg);
  }
  .banner {
    position: relative;
    width: 1200px;
    height: 328px;
    overflow: hidden;
    background: var(--bg);
  }
  .maple-art {
    position: absolute;
    left: 0;
    top: 0;
    width: 380px;
    height: 328px;
    border-radius: 50%;
    background: radial-gradient(closest-side, rgba(255,255,255,0.09) 0%, rgba(255,255,255,0.04) 60%, rgba(255,255,255,0) 100%);
  }
  .grid-glow {
    position: absolute;
    left: 370px;
    top: 40px;
    width: 400px;
    height: 250px;
    border-radius: 50%;
    background: radial-gradient(closest-side, rgba(255,255,255,0.03) 0%, rgba(255,255,255,0.10) 55%, rgba(255,255,255,0) 100%);
  }
  .hummingbird-globe {
    position: absolute;
    left: 900px;
    top: 20px;
    width: 290px;
    height: 280px;
    border-radius: 50%;
    background: radial-gradient(closest-side, rgba(255,255,255,0.50) 0%, rgba(236,220,255,0.30) 45%, rgba(200,170,240,0.10) 75%, rgba(255,255,255,0) 100%);
  }
  .hud {
    position: absolute;
    inset: 0;
  }
  .channel-name {
    position: absolute;
    left: 372px;
    width: 430px;
    top: 150px;
    margin: 0;
    text-align: center;
    font-family: "Montserrat", sans-serif;
    font-weight: 600;
    font-size: 40px;
    line-height: 48px;
    letter-spacing: 2px;
    color: var(--glyph);
  }
</style>
</head>
<body>
  <main class="banner">
    <div class="maple-art" role="img" aria-label="Faint line illustration of maple leaves behind the left ring"></div>
    <div class="grid-glow" role="img" aria-label="Soft glowing tech grid pattern in the centre"></div>

    <svg class="hud" width="1200" height="328" viewBox="0 0 1200 328" aria-hidden="true">
      <g class="grid-lines" stroke="var(--line-soft)" stroke-width="1" fill="none">
        <line x1="0" y1="120" x2="1200" y2="120"/>
        <line x1="0" y1="205" x2="1200" y2="205"/>
        <line x1="0" y1="230" x2="380" y2="230"/>
        <line x1="380" y1="80" x2="760" y2="80"/>
        <rect x="380" y="76" width="110" height="28"/>
        <rect x="800" y="60" width="48" height="26"/>
        <rect x="40" y="150" width="26" height="16"/>
        <rect x="1174" y="58" width="14" height="14"/>
        <path d="M1130 34 v22 h20"/>
        <path d="M820 36 h24 v10"/>
      </g>
      <g class="pink-lines" stroke="var(--accent-pink)" stroke-width="1">
        <line x1="0" y1="228" x2="300" y2="228"/>
        <line x1="1010" y1="290" x2="1200" y2="290"/>
        <line x1="1100" y1="40" x2="1200" y2="40"/>
      </g>

      <g class="left-ring" fill="none" stroke="var(--line)">
        <circle cx="204" cy="166" r="136" stroke-width="8" stroke-opacity="0.5"/>
        <circle cx="204" cy="166" r="118" stroke-width="2"/>
        <circle cx="204" cy="166" r="84" stroke-width="1.5"/>
        <path d="M 90 100 A 130 130 0 0 1 270 52" stroke-width="10" stroke-opacity="0.35"/>
        <path d="M 330 200 A 130 130 0 0 1 260 284" stroke-width="10" stroke-opacity="0.35"/>
      </g>

      <g class="right-ring" fill="none" stroke="var(--line)">
        <circle cx="860" cy="162" r="36" stroke-width="6" stroke-opacity="0.6"/>
        <circle cx="860" cy="162" r="27" stroke-width="2"/>
        <path d="M 816 140 A 48 48 0 0 1 850 114" stroke-width="2"/>
        <path d="M 904 184 A 48 48 0 0 1 870 210" stroke-width="2"/>
      </g>

      <g class="arrows" fill="var(--glyph-soft)">
        <polygon points="199,160 207,166 199,172"/>
        <polygon points="272,154 288,166 272,178" fill-opacity="0.5"/>
        <polygon points="762,60 780,74 762,88" fill-opacity="0.6"/>
        <polygon points="796,76 804,82 796,88"/>
        <polygon points="826,76 834,82 826,88"/>
        <polygon points="838,60 856,74 838,88" fill-opacity="0.6"/>
        <polygon points="808,232 816,238 808,244"/>
        <polygon points="838,232 846,238 838,244"/>
        <g>
          <polygon points="782,102 788,106 782,110"/>
          <polygon points="792,102 798,106 792,110"/>
          <polygon points="802,102 808,106 802,110"/>
          <polygon points="812,102 818,106 812,110"/>
          <polygon points="822,102 828,106 822,110"/>
          <polygon points="832,102 838,106 832,110"/>
          <polygon points="842,102 848,106 842,110"/>
          <polygon points="852,102 858,106 852,110"/>
        </g>
        <g fill-opacity="0.7">
          <polygon points="846,88 850,90 846,92"/>
          <polygon points="852,88 856,90 852,92"/>
          <polygon points="858,88 862,90 858,92"/>
          <polygon points="864,88 868,90 864,92"/>
          <polygon points="870,88 874,90 870,92"/>
          <polygon points="876,88 880,90 876,92"/>
          <polygon points="876,96 880,98 876,100"/>
          <polygon points="870,96 874,98 870,100"/>
        </g>
        <g>
          <polygon points="846,245 852,249 846,253"/>
          <polygon points="856,245 862,249 856,253"/>
          <polygon points="866,245 872,249 866,253"/>
          <polygon points="876,245 882,249 876,253"/>
          <polygon points="888,245 894,249 888,253"/>
          <polygon points="900,245 906,249 900,253"/>
          <polygon points="918,245 924,249 918,253"/>
          <polygon points="936,245 942,249 936,253"/>
        </g>
        <g fill-opacity="0.7">
          <polygon points="822,256 826,258 822,260"/>
          <polygon points="828,256 832,258 828,260"/>
          <polygon points="834,256 838,258 834,260"/>
          <polygon points="840,256 844,258 840,260"/>
          <polygon points="852,256 856,258 852,260"/>
          <polygon points="864,256 868,258 864,260"/>
          <polygon points="878,264 882,266 878,268"/>
          <polygon points="892,264 896,266 892,268"/>
          <polygon points="820,284 824,286 820,288"/>
          <polygon points="836,284 840,286 836,288"/>
        </g>
      </g>
    </svg>

    <div class="hummingbird-globe" role="img" aria-label="White line-art hummingbird hovering over a sparkling particle globe"></div>

    <h1 class="channel-name">LP Thornbury</h1>
  </main>
</body>
</html>
```